Lurin Dasko Website

Website for my son who is in 7th grade in the US. This will prepare him to show people his accomplishments when applying for a job or going to college. It should have:
* A picture (or multiple pictures)
* A resume page
* A place to share your accomplishments
* Links to his other social profiles
* A contact form

Great to include:
* Internships (show some photos of it along with what you’ve learned).
* Volunteer work.
* A side hustle that you want to highlight

Website sample I like:
https://brisatoleno.folivane.net/brisatolenomurga

Target Market(s)

For jobs and colleges admissions.

Number of Pages Required

5+ page

Colors

Designer to choose colors to be used in the design.

Requirements
Must have
• * A picture (or multiple pictures)
• * A resume page
• * A place to share your accomplishments
• * Links to his other social profiles
• * A contact form
Nice to have
• Great to include:
• * Internships (show some photos of it along with what you’ve learned).
• * Volunteer work.
• * A side hustle that you want to highlight

```html
<!DOCTYPE html>
<html lang="en">
<head>
<meta charset="utf-8">
<title>Lurin Dasko</title>
<link href="https://fonts.googleapis.com/css2?family=Montserrat:wght@500;600;700&family=Lato:wght@400;700&display=swap" rel="stylesheet">
<style>
:root{
  --orange:#f5a623;
  --ink:#3a3a3a;
  --text:#555;
  --muted:#666;
  --light:#f5f5f5;
  --white:#fff;
  --night:#2b2e33;
  --heading:Montserrat, sans-serif;
  --body:Lato, sans-serif;
}
*{box-sizing:border-box;margin:0;padding:0}
html,body{width:1200px;height:3360px;overflow:hidden}
body{position:relative;background:var(--light);font-family:var(--body);color:var(--text)}
.abs{position:absolute}
.top-rule{left:0;top:0;width:1200px;height:5px;background:var(--orange);z-index:3}
.header-band{left:0;top:0;width:1200px;height:593px;background:linear-gradient(180deg,#3d3f44 0%,#4a4740 35%,#6a5640 60%,#2f3138 100%)}
.brand{left:170px;top:48px;font-family:var(--heading);font-weight:700;font-size:35px;color:var(--orange);letter-spacing:.5px}
.nav{top:60px;font-family:var(--body);font-weight:700;font-size:14px;color:var(--white);text-transform:uppercase}
.nav.active{color:var(--orange)}
.login{left:941px;top:53px;width:85px;height:34px;border:2px solid var(--orange);border-radius:17px;color:var(--orange);font-weight:700;font-size:14px;display:flex;align-items:center;justify-content:center}
.hero{left:171px;top:186px;width:855px;height:512px;box-shadow:0 12px 24px rgba(0,0,0,.18)}
.hero-photo{left:0;top:0;width:855px;height:512px;background:linear-gradient(100deg,#d9cfc0 0%,#e9e2d6 35%,#f3efe8 60%,#fbfaf7 100%)}
.hero-title{left:516px;top:124px;font-family:var(--heading);font-weight:600;font-size:45px;color:var(--ink)}
.hero-sub{left:516px;top:186px;width:300px;font-size:25px;line-height:35px;color:var(--ink)}
.btn{background:var(--orange);color:var(--white);font-family:var(--body);font-weight:700;font-size:12px;border-radius:20px;display:flex;align-items:center;justify-content:center;text-transform:uppercase}
.hero .btn{left:516px;top:307px;width:106px;height:36px}
.dots{left:409px;top:484px;display:flex;gap:5px}
.dots i{width:8px;height:8px;border-radius:50%;background:#777;display:block}
.dots i:first-child{background:var(--orange)}
.sec-title{font-family:var(--heading);font-weight:600;font-size:33px;color:var(--ink)}
.center{left:0;width:1200px;text-align:center}
.lead{font-size:12px;line-height:21px;color:var(--muted)}
.acc-title{left:170px;top:780px}
.acc-text{left:170px;top:832px;width:300px;z-index:2}
.acc-photo{left:39px;top:945px;width:261px;height:168px;background:linear-gradient(180deg,#ece8e2 0%,#e6e2dc 60%,#dde2ea 100%)}
.acc-card{width:240px;height:93px;background:var(--white);border:2px solid #ebebeb;display:flex;align-items:center}
.acc-card .ico{margin-left:23px;width:47px;height:47px;border-radius:50%;background:var(--orange);display:flex;align-items:center;justify-content:center;flex:none}
.acc-card p{margin-left:14px;font-size:13.5px;line-height:17px;color:var(--ink)}
.white-band{left:0;width:1200px;background:var(--white)}
.intern-card{width:412px;height:209px;background:var(--white);border:2px solid #ececec}
.intern-card h3{position:absolute;left:31px;top:32px;width:180px;font-family:var(--heading);font-weight:600;font-size:18px;line-height:17px;color:var(--orange)}
.intern-card p{position:absolute;left:31px;top:80px;width:185px;font-size:11.5px;line-height:21px;color:var(--muted)}
.intern-card .pic{position:absolute;left:233px;top:23px;width:168px;height:168px;border-radius:50%;border:4px solid #f4e3c3}
.vol-photo{position:absolute}
.vol-text{left:674px;top:2008px;width:346px;font-size:11.5px;line-height:21px;color:var(--muted)}
.vol-btn{left:673px;top:2215px;width:105px;height:37px}
.vol-portrait{left:665px;top:2270px;width:483px;height:262px;background:linear-gradient(180deg,#eeeae5 0%,#e2d6c8 40%,#a9b4c8 75%,#7c8fb0 100%)}
.social{top:2728px;width:88px;height:88px;border-radius:50%;background:var(--night);color:var(--white);font-weight:700;font-size:13px;display:flex;align-items:center;justify-content:center}
.contact-band{left:0;top:2890px;width:1200px;height:409px;background:linear-gradient(180deg,#2e3036 0%,#3a3c42 60%,#25272c 100%)}
.field{background:var(--white);border:1px solid #ddd;font-size:11px;color:#333;padding:0 11px;display:flex;align-items:center;justify-content:space-between}
.field.tall{align-items:flex-start;padding-top:13px}
.submit{left:540px;top:3197px;width:122px;height:37px;font-size:13px}
.footer{left:0;top:3299px;width:1200px;height:61px;background:var(--white);text-align:center;font-size:11px;color:#444;padding-top:23px}
</style>
</head>
<body>
<div class="abs top-rule"></div>
<header>
  <div class="abs header-band" role="img" aria-label="Evening city skyline with tall towers"></div>
  <div class="abs brand">Lurin Dasko</div>
  <nav>
    <span class="abs nav active" style="left:466px">Home</span>
    <span class="abs nav" style="left:545px">About</span>
    <span class="abs nav" style="left:633px">Resume</span>
    <span class="abs nav" style="left:726px">Internships</span>
    <span class="abs nav" style="left:852px">Contact</span>
    <span class="abs login">LOGIN</span>
  </nav>
</header>

<section class="abs hero">
  <div class="abs hero-photo" role="img" aria-label="Boy working on a laptop at a wooden table by a bright window"></div>
  <h1 class="abs hero-title">Lurin Dasko</h1>
  <p class="abs hero-sub">At vero eos et accusamus et iusto odio dignissios du cimus qui blanditii.</p>
  <span class="abs btn">Read More</span>
  <div class="abs dots"><i></i><i></i><i></i><i></i></div>
</section>

<section>
  <h2 class="abs sec-title acc-title">Accomplishments</h2>
  <div class="abs acc-photo" role="img" aria-label="Boy wearing a medal giving a thumbs up"></div>
  <p class="abs lead acc-text">At vero eos et accusamus et iusto odio dignissimos ducim us qui blanditiis praesentium voluptatum deleniti atque corrupti quos dolores et quas molestias excepturi sint occaecati cupiditate non provident, similique sunt in cul pa qui officia deserunt mollitia animi,</p>
  <div class="abs acc-card" style="left:531px;top:793px">
    <span class="ico"><svg width="20" height="20" viewBox="0 0 20 20"><path d="M5 2h10v4a5 5 0 0 1-10 0z M3 3h2v3H3z M15 3h2v3h-2z M9 11h2v4H9z M6 15h8v3H6z" fill="#fff"/></svg></span>
    <p>At vero eos et accu<br>samus et iusto</p>
  </div>
  <div class="abs acc-card" style="left:786px;top:793px">
    <span class="ico"><svg width="20" height="20" viewBox="0 0 20 20"><path d="M18 2 2 9l6 2 2 7z" fill="#fff"/></svg></span>
    <p>At vero eos et accu<br>samus et iusto</p>
  </div>
  <div class="abs acc-card" style="left:531px;top:905px">
    <span class="ico"><svg width="20" height="20" viewBox="0 0 20 20"><circle cx="10" cy="6" r="4" fill="#fff"/><path d="M3 18a7 6 0 0 1 14 0z" fill="#fff"/></svg></span>
    <p>At vero eos et accu<br>samus et iusto</p>
  </div>
  <div class="abs acc-card" style="left:786px;top:905px">
    <span class="ico"><svg width="20" height="20" viewBox="0 0 20 20"><path d="M12 3l6 6-6 6v-4C7 11 4 13 2 17c0-6 4-10 10-10z" fill="#fff"/></svg></span>
    <p>At vero eos et accu<br>samus et iusto</p>
  </div>
</section>

<section>
  <div class="abs white-band" style="top:1113px;height:726px"></div>
  <h2 class="abs sec-title center" style="top:1168px">Internships</h2>
  <p class="abs lead" style="left:350px;top:1216px;width:500px;text-align:center">At vero eos et accusamus et iusto odio dignissimos ducimus qui blanditiis praesentium volu ptatum deleniti atque At vero eos et accusamus et iusto odio dignissimos ducimus qui blanditiis praesentium voluptatum deleniti atque corrupti quos dolorcorrupti quos dolor.</p>
  <div class="abs intern-card" style="left:171px;top:1301px">
    <h3>At vero eos accu samus eusto</h3>
    <p>At vero eos et accusamus et iusto odio dignissimos ducimus qui bla nditiis praesentium voluptatum deleniti atque corrup.</p>
    <div class="pic" role="img" aria-label="Boy thinking at a desk" style="background:linear-gradient(135deg,#8a7d6e,#d8cfc4)"></div>
  </div>
  <div class="abs intern-card" style="left:614px;top:1301px">
    <h3>At vero eos accu samus eusto</h3>
    <p>At vero eos et accusamus et iusto odio dignissimos ducimus qui bla nditiis praesentium voluptatum deleniti atque corrup.</p>
    <div class="pic" role="img" aria-label="Boy writing at a classroom desk" style="background:linear-gradient(135deg,#a07a5a,#3e4a6e)"></div>
  </div>
  <div class="abs intern-card" style="left:171px;top:1524px">
    <h3>At vero eos accu samus eusto</h3>
    <p>At vero eos et accusamus et iusto odio dignissimos ducimus qui bla nditiis praesentium voluptatum deleniti atque corrup.</p>
    <div class="pic" role="img" aria-label="Smiling boy giving a thumbs up" style="background:linear-gradient(135deg,#e8eef2,#4c5a78)"></div>
  </div>
  <div class="abs intern-card" style="left:614px;top:1524px">
    <h3>At vero eos accu samus eusto</h3>
    <p>At vero eos et accusamus et iusto odio dignissimos ducimus qui bla nditiis praesentium voluptatum deleniti atque corrup.</p>
    <div class="pic" role="img" aria-label="Boy on a video call with a laptop" style="background:linear-gradient(135deg,#e6e6e6,#2f4f8a)"></div>
  </div>
</section>

<section>
  <h2 class="abs sec-title center" style="top:1915px">Volunteer Work</h2>
  <div class="vol-photo" role="img" aria-label="Teen volunteer collecting litter in a park" style="left:171px;top:1970px;width:222px;height:212px;background:linear-gradient(135deg,#5f8a4a,#c9d3c2 55%,#3c5da0)"></div>
  <div class="vol-photo" role="img" aria-label="Young volunteers in blue shirts outdoors" style="left:407px;top:2004px;width:220px;height:214px;background:linear-gradient(135deg,#7a9a5a,#6aa8d8 70%,#3a86c8)"></div>
  <div class="vol-photo" role="img" aria-label="Boy picking up trash on a grassy hill" style="left:170px;top:2202px;width:220px;height:214px;background:linear-gradient(135deg,#8bae62,#c8c8c0 60%,#2a2a2a)"></div>
  <div class="vol-photo" role="img" aria-label="Boy holding a box for recycling plastic" style="left:400px;top:2235px;width:222px;height:215px;background:linear-gradient(135deg,#4a7a3a,#d9d2c0 65%,#8a6a4a)"></div>
  <p class="abs vol-text">At vero eos et accusamus et iusto odio dignissimos ducimus qui blanditiis praesentium voluptatum deleniti atque At vero eos et accusamus et iusto odio dignissimos ducimus qui blanditiis praes entium voluptatum deleniti atque corrupti quos dolorcorrupti qu odoAt vero eos et accusamus et iusto odio dignissimos ducimus qui blanditiis praesentium voluptatum deleniti atque At vero eos et accusamus et iusto odio dignissimos ducimus qui blanditiis praese ntium voluptatum deleniti atque corrupti quos dolorcorrupti quos doloror.</p>
  <span class="abs btn vol-btn">Read More</span>
  <div class="abs vol-portrait" role="img" aria-label="Portrait of a teen boy in a blue checked shirt"></div>
</section>

<section>
  <div class="abs white-band" style="top:2532px;height:358px"></div>
  <h2 class="abs sec-title center" style="top:2600px">Social Media</h2>
  <p class="abs lead" style="left:350px;top:2648px;width:500px;text-align:center">At vero eos et accusamus et iusto odio dignissimos ducimus qui blanditiis praesentium volu ptatum deleniti atque At vero eos et accusamus et iusto odio dignissimos ducimus</p>
  <a class="abs social" style="left:395px">Chatterly</a>
  <a class="abs social" style="left:502px">Peepnet</a>
  <a class="abs social" style="left:609px">Workhub</a>
  <a class="abs social" style="left:716px">Circlet</a>
</section>

<section>
  <div class="abs contact-band" role="img" aria-label="Dark city skyline at night"></div>
  <h2 class="abs sec-title center" style="top:2935px;color:var(--white)">Contact Us</h2>
  <p class="abs lead" style="left:350px;top:2983px;width:500px;text-align:center;color:var(--white)">At vero eos et accusamus et iusto odio dignissimos ducimus qui blanditiis praesentium volu ptatum deleniti atque At vero eos et accusamus et iusto odio dignissimos ducimus</p>
  <div class="abs field" style="left:292px;top:3052px;width:304px;height:39px">Name:<svg width="10" height="10" viewBox="0 0 10 10"><circle cx="5" cy="3" r="2.2" fill="#bbb"/><path d="M1 10a4 4 0 0 1 8 0z" fill="#bbb"/></svg></div>
  <div class="abs field" style="left:292px;top:3098px;width:304px;height:39px">Email:<svg width="12" height="9" viewBox="0 0 12 9"><rect width="12" height="9" fill="#bbb"/><path d="M0 0l6 5 6-5" stroke="#fff" fill="none"/></svg></div>
  <div class="abs field" style="left:292px;top:3145px;width:304px;height:39px">Phone:<svg width="10" height="10" viewBox="0 0 10 10"><path d="M2 0l2 3-1 1c1 2 2 3 3 3l1-1 3 2-1 2C4 10 0 6 0 2z" fill="#bbb"/></svg></div>
  <div class="abs field tall" style="left:604px;top:3052px;width:304px;height:132px">Subject:<svg width="11" height="11" viewBox="0 0 11 11"><rect width="11" height="11" fill="#bbb"/><path d="M3 8l5-5" stroke="#fff"/></svg></div>
  <span class="abs btn submit">Submit</span>
</section>

<footer class="abs footer">Copyright 2019 All Rights Reserved</footer>
</body>
</html>
```